Employee Benefits Flyer for Recruiting

We are a Steel Product Supplier and Manufacturer in Toledo Ohio.

We would like to create an "attention getting", one-page handout to give prospective employees (both production and administrative) that illustrates all the benefits we offer as a company. An editable document would be preferable as we add more or change existing benefits in the future. Current benefits include:

Individual and Family Medical Insurance
Dental Insurance
Vision Insurance
Short Term Disability Insurance
Critical Illness and Accident Insurance
No Cost Life Insurance Policy
Education Cost Reimbursement
401K with Company Match
Profit Sharing
Attendance and Performance Bonuses
No Cost Legal Assistance
No Cost Counseling Services
No Cost Tobacco Cessation Coaching
No Cost College Planning Assistance
No Cost Work-Life Services
No Cost Employee Discounts
No Cost Legal Consultation
No Cost Financial Consultation
No Cost ID Theft Assistance
No Cost Tax Consultation Assistance
Up to 17 Days of Paid Time Off

Target Market(s)

Potential Employees

Industry/Entity Type

Industrial Manufacturing

Requirements
Must have
• Nicely laid out illustrations / engaging content

```html
<!DOCTYPE html>
<html lang="en">
<head>
<meta charset="utf-8">
<title>Keystone Steel Works – Employee Benefits</title>
<link href="https://fonts.googleapis.com/css2?family=Oswald:wght@500;600&family=Roboto+Condensed:wght@600&display=swap" rel="stylesheet">
<style>
  :root{
    --blue:#1f5fc8;
    --blue-top:#2f80e2;
    --blue-bottom:#1b4ea9;
    --ink:#27313f;
    --ink-dark:#1b222d;
    --white:#ffffff;
    --steel:#3a4553;
  }
  *{margin:0;padding:0;box-sizing:border-box}
  html,body{width:1003px;height:1200px;overflow:hidden;background:var(--white)}
  .flyer{position:relative;width:1003px;height:1200px;background:var(--white);overflow:hidden}

  .brand{position:absolute;left:0;top:0;width:485px;height:332px;display:flex;flex-direction:column;align-items:center;justify-content:center;gap:22px}
  .brand-mark{width:120px;height:120px;border-radius:50%;background:var(--blue)}
  .brand-name{font-family:"Oswald",sans-serif;font-weight:600;font-size:34px;letter-spacing:1px;color:var(--blue);text-transform:uppercase}

  .site-photo{position:absolute;left:0;top:332px;width:1003px;height:682px;
    background:linear-gradient(180deg,#d9dde0 0%,#9fb3c6 18%,#2f6fb8 35%,#8d949a 55%,#3b6fb8 72%,#5d7b4a 88%,#7d8f55 100%)}
  .site-photo-fade{position:absolute;left:934px;top:332px;width:69px;height:682px;
    background:linear-gradient(180deg,rgba(255,255,255,.15),rgba(255,255,255,0) 40%,rgba(255,255,255,.9) 100%)}

  .contact{position:absolute;left:0;top:1014px;width:485px;height:130px;background:linear-gradient(90deg,var(--ink-dark),var(--ink));
    display:flex;flex-direction:column;justify-content:center;padding-left:48px;color:var(--white);font-family:"Oswald",sans-serif}
  .contact-phone{font-size:50px;font-weight:600;line-height:1.05;letter-spacing:-.5px}
  .contact-web{font-size:27px;font-weight:500;line-height:1.15;letter-spacing:-.3px}

  .benefits{position:absolute;left:485px;top:0;width:469px;height:1200px;background:linear-gradient(180deg,var(--blue-top),var(--blue) 55%,var(--blue-bottom))}

  .ribbon{position:absolute;left:460px;top:47px;width:526px;height:59px;background:var(--ink);
    display:flex;align-items:center;justify-content:center;font-family:"Oswald",sans-serif;font-weight:600;font-size:40px;color:var(--white);letter-spacing:-.5px;z-index:2}
  .ribbon-fold{position:absolute;z-index:1}
  .ribbon-fold--top{left:954px;top:27px}
  .ribbon-fold--bottom{left:460px;top:106px}

  .benefit-grid{position:absolute;left:510px;top:143px;width:430px;display:grid;grid-template-columns:repeat(3,1fr);grid-auto-rows:144px}
  .benefit{display:flex;flex-direction:column;align-items:center;text-align:center}
  .benefit-icon{width:86px;height:86px;border-radius:50%;background:var(--white);display:flex;align-items:center;justify-content:center;box-shadow:0 2px 4px rgba(0,0,0,.2)}
  .benefit-icon svg{width:48px;height:48px;fill:var(--blue)}
  .benefit-label{margin-top:10px;font-family:"Roboto Condensed",sans-serif;font-weight:600;font-size:13.5px;line-height:1.08;color:var(--white);white-space:nowrap}
</style>
</head>
<body>
<main class="flyer">
  <header class="brand">
    <span class="brand-mark" aria-hidden="true"></span>
    <span class="brand-name">Keystone Steel Works</span>
  </header>

  <div class="site-photo" role="img" aria-label="Aerial photograph of the company's blue steel-clad plant building with rooftop units and lawn"></div>
  <div class="site-photo-fade" aria-hidden="true"></div>

  <section class="contact">
    <p class="contact-phone">CALL 555-014-2286</p>
    <p class="contact-web">WWW.KEYSTONESTEELWORKS.COM</p>
  </section>

  <section class="benefits" aria-label="Benefits"></section>

  <svg class="ribbon-fold ribbon-fold--top" width="32" height="20" aria-hidden="true"><polygon points="0,0 0,20 32,20" fill="#3b4656"/></svg>
  <svg class="ribbon-fold ribbon-fold--bottom" width="25" height="20" aria-hidden="true"><polygon points="0,0 25,0 25,20" fill="#141a22"/></svg>
  <h1 class="ribbon">WE OFFER THE BENEFITS</h1>

  <ul class="benefit-grid">
    <li class="benefit"><span class="benefit-icon"><svg viewBox="0 0 48 48"><circle cx="24" cy="14" r="6"/><circle cx="11" cy="22" r="5"/><circle cx="37" cy="22" r="5"/><path d="M14 44v-8a10 10 0 0 1 20 0v8zM2 44v-6a9 9 0 0 1 10-9v15zM46 44v-6a9 9 0 0 0-10-9v15z"/></svg></span><span class="benefit-label">Individual &amp; Family<br>Medical Insurance</span></li>
    <li class="benefit"><span class="benefit-icon"><svg viewBox="0 0 48 48"><path d="M10 6c6-3 10 2 14 0s9-3 14 0c5 4 2 14 0 18-2 6-2 20-6 20s-3-12-8-12-4 12-8 12-4-14-6-20C8 20 5 10 10 6z"/></svg></span><span class="benefit-label">Dental<br>Insurance</span></li>
    <li class="benefit"><span class="benefit-icon"><svg viewBox="0 0 48 48"><path d="M2 24C10 12 38 12 46 24 38 36 10 36 2 24z"/><circle cx="24" cy="24" r="8" fill="#fff"/><circle cx="24" cy="24" r="4"/></svg></span><span class="benefit-label">Vision<br>Insurance</span></li>

    <li class="benefit"><span class="benefit-icon"><svg viewBox="0 0 48 48"><polygon points="24,4 46,13 24,22 2,13"/><circle cx="24" cy="34" r="11"/><text x="24" y="40" font-size="16" text-anchor="middle" fill="#fff" font-family="sans-serif" font-weight="bold">$</text></svg></span><span class="benefit-label">Education Cost<br>Reimbursement</span></li>
    <li class="benefit"><span class="benefit-icon"><svg viewBox="0 0 48 48"><path d="M12 4h16v8a4 4 0 1 1 0 8v4h8v8a4 4 0 1 0 0 8v4H12V30a4 4 0 1 0 0-8z"/></svg></span><span class="benefit-label">401K with<br>Company Match</span></li>
    <li class="benefit"><span class="benefit-icon"><svg viewBox="0 0 48 48"><path d="M22 8A18 18 0 1 0 40 26H22z"/><path d="M27 3a18 18 0 0 1 18 18H27z"/></svg></span><span class="benefit-label">Profit<br>Sharing</span></li>

    <li class="benefit"><span class="benefit-icon"><svg viewBox="0 0 48 48"><rect x="2" y="30" width="34" height="8"/><rect x="38" y="30" width="4" height="8"/><path d="M40 8c-4 5 4 9 0 18M45 6c-4 5 4 10 0 20" stroke="#1f5fc8" stroke-width="2.5" fill="none"/></svg></span><span class="benefit-label">No Cost Tobacco<br>Cessation Coaching</span></li>
    <li class="benefit"><span class="benefit-icon"><svg viewBox="0 0 48 48"><polygon points="24,8 47,18 24,28 1,18"/><path d="M11 24v10c6 6 20 6 26 0V24l-13 6z"/><rect x="6" y="19" width="2" height="18"/></svg></span><span class="benefit-label">No Cost College<br>Planning Assistance</span></li>
    <li class="benefit"><span class="benefit-icon"><svg viewBox="0 0 48 48"><path d="M17 8h14v6h-3v-3h-8v3h-3z"/><rect x="3" y="14" width="42" height="28" rx="4"/><rect x="3" y="25" width="42" height="2" fill="#fff"/></svg></span><span class="benefit-label">No Cost Work-<br>Life Services</span></li>

    <li class="benefit"><span class="benefit-icon"><svg viewBox="0 0 48 48"><rect x="3" y="14" width="42" height="28" rx="4"/><rect x="8" y="20" width="12" height="14" fill="#fff"/><rect x="24" y="21" width="16" height="3" fill="#fff"/><rect x="24" y="28" width="16" height="3" fill="#fff"/><path d="M24 14V4" stroke="#1f5fc8" stroke-width="2"/></svg></span><span class="benefit-label">No Cost ID<br>Theft Assistance</span></li>
    <li class="benefit"><span class="benefit-icon"><svg viewBox="0 0 48 48"><path d="M8 3h24v42H8z" fill="none" stroke="#1f5fc8" stroke-width="2.5"/><rect x="13" y="10" width="14" height="2.5"/><rect x="13" y="17" width="10" height="2.5"/><circle cx="30" cy="30" r="8" fill="#fff" stroke="#1f5fc8" stroke-width="2.5"/><path d="M35 36l8 8" stroke="#1f5fc8" stroke-width="3"/></svg></span><span class="benefit-label">No Cost Tax<br>Consultation Assistance</span></li>
    <li class="benefit"><span class="benefit-icon"><svg viewBox="0 0 48 48"><path d="M18 14a14 10 0 0 1 28 0z"/><rect x="31" y="14" width="2" height="20"/><path d="M2 28l8 8h24v4H8L0 30z"/><rect x="8" y="40" width="3" height="6"/><rect x="28" y="40" width="3" height="6"/></svg></span><span class="benefit-label">Up to 17 Days<br>of Paid Time Off</span></li>

    <li class="benefit"><span class="benefit-icon"><svg viewBox="0 0 48 48"><circle cx="26" cy="6" r="4"/><path d="M24 12h4v10h8v4H24z"/><path d="M2 36c8-4 14-4 20 0h14c4 0 4 4 0 4H20v2c10 0 18-2 26-8v-4c-8 4-14 6-20 6" fill="none" stroke="#1f5fc8" stroke-width="3"/></svg></span><span class="benefit-label">Short Term<br>Disability Insurance</span></li>
    <li class="benefit"><span class="benefit-icon"><svg viewBox="0 0 48 48"><circle cx="16" cy="8" r="6"/><path d="M6 44V24a10 10 0 0 1 20 0v20z"/><path d="M34 18l12 4v8c0 8-6 12-12 14-6-2-12-6-12-14v-8z"/><path d="M28 30l4 4 8-8" stroke="#fff" stroke-width="3" fill="none"/></svg></span><span class="benefit-label">Critical Illness &amp;<br>Accident Insurance</span></li>
    <li class="benefit"><span class="benefit-icon"><svg viewBox="0 0 48 48"><path d="M24 2l20 8v12c0 12-9 20-20 24C13 42 4 34 4 22V10z"/><circle cx="24" cy="20" r="5" fill="#fff"/><path d="M15 34a9 9 0 0 1 18 0z" fill="#fff"/></svg></span><span class="benefit-label">No Cost Life<br>Insurance Policy</span></li>

    <li class="benefit"><span class="benefit-icon"><svg viewBox="0 0 48 48"><circle cx="20" cy="12" r="7" fill="none" stroke="#1f5fc8" stroke-width="3.5"/><path d="M4 42a16 16 0 0 1 26-12" fill="none" stroke="#1f5fc8" stroke-width="3.5"/><path d="M4 42h20M30 38l5 5 9-9" fill="none" stroke="#1f5fc8" stroke-width="3.5"/></svg></span><span class="benefit-label">Attendance and<br>Performance Bonuses</span></li>
    <li class="benefit"><span class="benefit-icon"><svg viewBox="0 0 48 48"><rect x="18" y="4" width="12" height="22" rx="2" transform="rotate(45 24 15)"/><rect x="24" y="20" width="20" height="5" transform="rotate(45 34 22)"/><rect x="4" y="38" width="22" height="6" rx="2"/></svg></span><span class="benefit-label">No Cost<br>Legal Assistance</span></li>
    <li class="benefit"><span class="benefit-icon"><svg viewBox="0 0 48 48"><rect x="14" y="2" width="20" height="8" rx="2"/><circle cx="12" cy="20" r="5"/><circle cx="36" cy="20" r="5"/><path d="M4 38v-6a8 8 0 0 1 16 0v6zM28 38v-6a8 8 0 0 1 16 0v6z"/><rect x="2" y="40" width="44" height="4"/></svg></span><span class="benefit-label">No Cost<br>Counseling Services</span></li>

    <li class="benefit"><span class="benefit-icon"><svg viewBox="0 0 48 48"><circle cx="13" cy="16" r="5"/><circle cx="35" cy="16" r="5"/><path d="M4 32a9 9 0 0 1 18 0zM26 32a9 9 0 0 1 18 0z"/><path d="M10 8a16 16 0 0 1 28 0M38 40a16 16 0 0 1-28 0" fill="none" stroke="#1f5fc8" stroke-width="3"/></svg></span><span class="benefit-label">No Cost Employee<br>Discounts</span></li>
    <li class="benefit"><span class="benefit-icon"><svg viewBox="0 0 48 48"><circle cx="18" cy="14" r="8"/><path d="M2 46v-8a16 16 0 0 1 32 0v8z"/><rect x="30" y="2" width="16" height="12" rx="2"/></svg></span><span class="benefit-label">No Cost Legal<br>Consultation</span></li>
    <li class="benefit"><span class="benefit-icon"><svg viewBox="0 0 48 48"><circle cx="18" cy="14" r="8"/><path d="M2 46v-8a16 16 0 0 1 32 0v8z"/><circle cx="36" cy="30" r="8" fill="#fff" stroke="#1f5fc8" stroke-width="2.5"/><text x="36" y="35" font-size="13" text-anchor="middle" font-family="sans-serif" font-weight="bold" fill="#1f5fc8">$</text></svg></span><span class="benefit-label">No Cost Financial<br>Consultation</span></li>
  </ul>
</main>
</body>
</html>
```